Business card for medical clinic

I need an upmarket, modern medical/health business card for my clinic

Contact Information for Business Card

name, address, email, qr code

```html
<!DOCTYPE html>
<html lang="en">
<head>
<meta charset="UTF-8">
<title>Meridian Care Clinic – Business Card</title>
<link rel="stylesheet" href="https://fonts.googleapis.com/css2?family=Cinzel:wght@500&family=Arimo:wght@400&display=swap">
<style>
  :root {
    --backdrop: #9c9c9c;
    --paper: #f7f7f6;
    --brand-blue: #2f8fcc;
    --deep-blue: #145a87;
    --edge-blue: #2a8ac6;
    --ink: #3b3b3b;
    --white: #ffffff;
  }
  * { box-sizing: border-box; margin: 0; padding: 0; }
  html, body {
    width: 1200px; height: 1020px; overflow: hidden;
    background: var(--backdrop);
  }
  .canvas {
    position: relative; width: 1200px; height: 1020px;
  }
  .card {
    position: absolute; left: 206px;
    width: 788px; height: 450px;
    box-shadow: 0 14px 30px rgba(0,0,0,0.25);
  }
  .card-front {
    top: 35px; background: var(--paper);
    border-bottom: 8px solid var(--edge-blue);
  }
  .card-back {
    top: 535px; background: var(--deep-blue);
    display: flex; align-items: center; justify-content: center;
  }
  .brand {
    display: flex; align-items: center; gap: 14px;
    font-family: "Cinzel", serif; font-weight: 500;
    letter-spacing: 0.04em; line-height: 1.1;
  }
  .brand-mark {
    flex: none; border-radius: 50%; border-style: solid;
  }
  .card-front .brand {
    position: absolute; left: 48px; top: 178px;
    color: var(--brand-blue); font-size: 27px;
  }
  .card-front .brand-mark {
    width: 64px; height: 64px; border-width: 3px; border-color: var(--brand-blue);
  }
  .card-back .brand { color: var(--white); font-size: 46px; gap: 22px; }
  .card-back .brand-mark {
    width: 104px; height: 104px; border-width: 4px; border-color: var(--white);
  }
  .divider {
    position: absolute; left: 400px; top: 105px;
    width: 1.5px; height: 240px; background: var(--brand-blue);
  }
  .contact {
    position: absolute; left: 430px; top: 108px;
    font-family: "Arimo", sans-serif; color: var(--ink);
  }
  .person-name {
    font-family: "Cinzel", serif; font-weight: 500;
    color: var(--brand-blue); font-size: 30px; letter-spacing: 0.04em;
  }
  .person-title { font-size: 19px; margin-top: 2px; }
  .address { font-size: 20px; line-height: 1.3; margin-top: 22px; }
  .contact-list { list-style: none; margin-top: 18px; font-size: 20px; line-height: 1.55; }
  .contact-list li { display: flex; align-items: center; gap: 10px; }
  .contact-list svg { width: 16px; height: 16px; flex: none; }
</style>
</head>
<body>
<main class="canvas">
  <section class="card card-front" aria-label="Card front">
    <div class="brand">
      <span class="brand-mark"></span>
      <span>Meridian Care<br>Clinic</span>
    </div>
    <div class="divider"></div>
    <div class="contact">
      <h1 class="person-name">DANIEL HART</h1>
      <p class="person-title">Director/Founder</p>
      <p class="address">1870 Harbor Lane<br>Westfield AV 31870</p>
      <ul class="contact-list">
        <li>
          <svg viewBox="0 0 16 16" aria-hidden="true"><path fill="#2f8fcc" d="M2 6c0-2 2-3 6-3s6 1 6 3v1h-3V5.5H5V7H2zM4 8h8l1.5 5h-11z"/></svg>
          04718 392 6610
        </li>
        <li>
          <svg viewBox="0 0 16 16" aria-hidden="true"><rect x="1" y="3" width="14" height="10" rx="1" fill="#2f8fcc"/><path d="M1.5 3.8 8 9l6.5-5.2" fill="none" stroke="#fff" stroke-width="1.2"/></svg>
          info@meridiancareclinic.com
        </li>
        <li>
          <svg viewBox="0 0 16 16" aria-hidden="true"><circle cx="8" cy="8" r="7" fill="#2f8fcc"/><path d="M1 8h14M8 1c-3 3-3 11 0 14M8 1c3 3 3 11 0 14" fill="none" stroke="#fff" stroke-width="1"/></svg>
          www.meridiancareclinic.com
        </li>
      </ul>
    </div>
  </section>

  <section class="card card-back" aria-label="Card back">
    <div class="brand">
      <span class="brand-mark"></span>
      <span>Meridian Care<br>Clinic</span>
    </div>
  </section>
</main>
</body>
</html>
```